Grafik für Erste-Hilfe-Kurse gesucht
Zielgruppe
Berufliche Weiterbildung und Erste Hilfe Kurse
Aufgabenstellung
Eine Grafik die für Plakate und Flyer dient. Das Bild soll zur Werbung für Erste Hilfe am Kind, also für Eltern, Großeltern usw., verwendet werden. Es soll halt auffallen

```html
<!DOCTYPE html>
<html lang="de">
<head>
<meta charset="utf-8">
<title>Kurs Erste Hilfe am Kind – Plakat</title>
<link href="https://fonts.googleapis.com/css2?family=Open+Sans:wght@300;800&display=swap" rel="stylesheet">
<style>
  :root {
    --page-bg: #e4e4e6;
    --poster-gray: #414143;
    --poster-red: #d42b2d;
    --heart-red: rgba(196, 32, 38, 0.86);
    --white: #ffffff;
    --photo-light: #dfe6ee;
    --photo-warm: #f0c9a8;
  }
  html, body {
    margin: 0;
    width: 1200px;
    height: 900px;
    overflow: hidden;
    background: var(--page-bg);
  }
  .canvas {
    position: relative;
    width: 1200px;
    height: 900px;
  }
  .poster {
    position: absolute;
    left: 302px;
    top: 30px;
    width: 596px;
    height: 839px;
    display: block;
  }
  .headline {
    font-family: "Open Sans", sans-serif;
    fill: var(--white);
  }
  .headline-light { font-weight: 300; font-size: 33px; }
  .headline-bold { font-weight: 800; font-size: 45px; letter-spacing: 1px; }
</style>
</head>
<body>
<main class="canvas">
  <svg class="poster" viewBox="0 0 528 743" xmlns="http://www.w3.org/2000/svg">
    <defs>
      <clipPath id="poster-area"><rect width="528" height="743"/></clipPath>
      <linearGradient id="photo-tones" x1="0" y1="0" x2="0.6" y2="1">
        <stop offset="0" stop-color="#c9d5e2"/>
        <stop offset="0.45" stop-color="var(--photo-light)"/>
        <stop offset="0.8" stop-color="var(--photo-warm)"/>
        <stop offset="1" stop-color="#d8473c"/>
      </linearGradient>
    </defs>
    <g clip-path="url(#poster-area)">
      <rect class="poster-base" width="528" height="743" fill="var(--poster-gray)"/>
      <path class="red-field" d="M0,430 Q300,500 528,465 L528,743 L0,743 Z" fill="var(--poster-red)"/>
      <circle class="white-ring" cx="400" cy="120" r="340" fill="var(--white)"/>
      <circle class="course-photo" cx="440" cy="110" r="275" fill="url(#photo-tones)"
              role="img" aria-label="Foto: Kursleiterin übt Herzdruckmassage an einer Babypuppe"/>
      <path class="glow-arc" d="M-40,620 Q200,860 560,560" fill="none" stroke="rgba(255,255,255,0.14)" stroke-width="18"/>
      <path class="glow-arc" d="M40,20 Q200,-10 330,60" fill="none" stroke="rgba(255,255,255,0.12)" stroke-width="10"/>
      <path class="heart" d="M203,330 C170,285 130,268 95,270 C40,272 -5,320 -2,385 C2,470 120,560 203,685 C286,560 404,470 418,385 C425,320 370,272 312,270 C270,268 236,285 203,330 Z"
            fill="var(--heart-red)" stroke="var(--white)" stroke-width="3.5" stroke-linejoin="round"/>
      <g class="headline">
        <text class="headline-light" x="82" y="387">KURS</text>
        <text class="headline-bold" x="80" y="434">ERSTE</text>
        <text class="headline-bold" x="80" y="476">HILFE</text>
        <text class="headline-light" x="82" y="512">AM KIND</text>
      </g>
      <path class="first-aid-cross" d="M295,398 H321 V425 H348 V451 H321 V478 H295 V451 H268 V425 H295 Z" fill="var(--white)"/>
    </g>
  </svg>
</main>
</body>
</html>
```